Healthcare patient advocacy company needs banner for conference booth

We need a banner to hang behind us in our booth at conferences. I would like something that prominently features our company name - velorin LLC. And also includes the following language: No employee should face medical debt alone. No Plan should be unrepresented. Expert advocacy and legal support from first bill to final resolution. The colors we use for our other materials are HEX 002C45, FECC73, 00C6CF, E0D5B9, 004C66. And the font is Epilogue. I would welcome some graphics, but no scales of justice or dollar bills or anything like that. I'm attaching some materials so you can see one of our brochures.

Target Market(s)

B2B - health insurers, third-party health care administrators, cost-containment companies

Industry/Entity Type

Healthcare Advocacy

Requirements
Must have
• Name prominently displayed and taglines in project description.
Nice to have
• I would like something easy to read and eye-catching that is not overly complicated or cutsey.
Should not have
• Scales of justice or dollar signs.

```html
<!DOCTYPE html>
<html lang="en">
<head>
<meta charset="utf-8">
<title>velorin LLC — Conference Booth Banner</title>
<link rel="stylesheet" href="https://fonts.googleapis.com/css2?family=Epilogue:ital,wght@0,600;0,700;0,800;1,500;1,600&display=swap">
<style>
  :root {
    --navy: #0f2d44;
    --gold: #fccc76;
    --teal: #31b9c8;
    --sand: #e0d5b9;
    --deep-teal: #0f4f6b;
    --white: #ffffff;
    --page: #ffffff;
  }
  * { box-sizing: border-box; margin: 0; padding: 0; }
  html, body {
    width: 1200px;
    height: 690px;
    overflow: hidden;
    background: var(--page);
    font-family: "Epilogue", Arial, sans-serif;
  }
  .banner {
    position: absolute;
    left: 20px;
    top: 55px;
    width: 1160px;
    height: 580px;
    background: var(--navy);
    overflow: hidden;
  }
  .corner-arc {
    position: absolute;
    left: -233px;
    top: -233px;
    width: 466px;
    height: 466px;
    border-radius: 50%;
    background: var(--teal);
  }
  .brand-name {
    position: absolute;
    left: 0;
    width: 100%;
    top: 70px;
    padding-left: 22px;
    text-align: center;
    font-size: 100px;
    font-weight: 800;
    letter-spacing: -1px;
    color: var(--gold);
    line-height: 1;
  }
  .tagline {
    position: absolute;
    top: 230px;
    font-weight: 700;
    font-size: 39px;
    line-height: 44px;
    letter-spacing: -0.3px;
  }
  .tagline .lead { display: block; color: var(--white); }
  .tagline .accent { display: block; color: var(--teal); }
  .tagline--employee { right: calc(1160px - 632px); text-align: right; }
  .tagline--plan { left: 680px; text-align: left; }
  .tagline-divider {
    position: absolute;
    left: 653px;
    top: 232px;
    width: 6px;
    height: 74px;
    background: var(--gold);
  }
  .promise {
    position: absolute;
    left: 313px;
    top: 344px;
    width: 557px;
    height: 73px;
    border: 1.5px solid var(--teal);
    border-radius: 37px;
    display: flex;
    align-items: center;
    justify-content: center;
    text-align: center;
    font-style: italic;
    font-weight: 600;
    font-size: 27px;
    line-height: 32px;
    letter-spacing: -0.2px;
    color: var(--sand);
  }
  .motif-area {
    position: absolute;
    left: 815px;
    top: 459px;
    width: 287px;
    height: 70px;
    background: linear-gradient(90deg, var(--teal) 0%, var(--gold) 38%, var(--sand) 65%, var(--deep-teal) 100%);
    opacity: 0.9;
  }
</style>
</head>
<body>
  <main class="banner">
    <div class="corner-arc" aria-hidden="true"></div>

    <h1 class="brand-name">velorin LLC</h1>

    <p class="tagline tagline--employee">
      <span class="lead">No employee should</span>
      <span class="accent">face medical debt alone</span>
    </p>
    <div class="tagline-divider" aria-hidden="true"></div>
    <p class="tagline tagline--plan">
      <span class="lead">No Plan should be</span>
      <span class="accent">unrepresented.</span>
    </p>

    <p class="promise">Expert advocacy and legal support<br>from first bill to final resolution</p>

    <div class="motif-area" role="img" aria-label="Decorative row of geometric brand shapes in teal, gold, sand and deep teal"></div>
  </main>
</body>
</html>
```